Restaurant needs promotional material

We need a design for a "free welcome cocktail on your next visit" flyer. The flyer must have a black background and be contemporary. Our logo is the name of the restaurant which is "Ember Nook" in edwardian script font with italic selected.

There must be a section for terms and conditions, which are:
1 free cocktail for every main course ordered from our evening menu over the value of 9.95€ (not including taxes). The number of free cocktails cannot exceed the number of main courses ordered from your previous visit. This offer is only valid when you present both this flyer and your receipt from your previous visit. This offer does not include ice cream cocktails. This offer cannot be used in conjunction with any other offer or promotion. Limit 1 free cocktail per person. We reserve the right to final interpretation of this offer and can cancel the offer at any time.

A space must also be left where we can write a "valid until" date.

The uploaded photos are a picture of our cocktail menu and the publicity we are currently running, so you can get a feel for your design.

Thanks

Industry/Entity Type

Restaurant

Colors
000000

Requirements
Must have
• Also included in the flyer is the text " Please present this flyer along with your bill from your previous visit upon arrival.
• Pictures of cocktails!

```html
<!DOCTYPE html>
<html lang="en">
<head>
<meta charset="utf-8">
<title>Ember Nook – Free Welcome Cocktail Flyer</title>
<link href="https://fonts.googleapis.com/css2?family=Varela+Round&family=Arimo:wght@400;700&display=swap" rel="stylesheet">
<style>
  :root {
    --page-bg: #ffffff;
    --flyer-bg: #0b0606;
    --ink: #ffffff;
    --ink-soft: #ececec;
    --accent-red: #e81f36;
    --valid-bar: #5f5a59;
    --photo-dark: #120604;
    --photo-mid: #5a1a0c;
    --photo-warm: #a8341a;
  }
  * { margin: 0; padding: 0; box-sizing: border-box; }
  html, body {
    width: 1200px; height: 1200px; overflow: hidden;
    background: var(--page-bg);
  }
  .flyer {
    position: absolute;
    left: 335px; top: 40px;
    width: 565px; height: 1197px;
    transform: scale(0.936);
    transform-origin: 0 0;
    background: var(--flyer-bg);
    overflow: hidden;
    font-family: "Varela Round", sans-serif;
    color: var(--ink);
  }
  .brand-band {
    position: absolute; left: 232px; top: 118px;
    width: 333px; height: 57px;
    background: var(--accent-red);
  }
  .brand-name {
    position: absolute; font-size: 54px; line-height: 1; color: var(--ink);
  }
  .brand-name--top { left: 80px; top: 62px; }
  .brand-name--bottom { left: 92px; top: 160px; }
  .brand-tag {
    position: absolute; left: 173px; top: 136px;
    font-family: "Arimo", sans-serif; font-weight: 700;
    font-size: 20px; letter-spacing: 0.5px; color: var(--ink);
  }
  .headline {
    position: absolute; right: 50px; top: 256px;
    text-align: right; line-height: 1; font-weight: 400;
  }
  .headline__free { font-size: 72px; letter-spacing: 1px; }
  .headline__main { font-size: 54px; margin-top: -4px; letter-spacing: -0.5px; }
  .headline__sub { font-size: 38px; }
  .photo {
    position: absolute; left: 0; top: 410px;
    width: 565px; height: 450px;
    background:
      radial-gradient(ellipse 55% 40% at 55% 55%, var(--photo-warm) 0%, rgba(120,30,14,0.6) 45%, transparent 80%),
      linear-gradient(180deg, var(--photo-dark) 0%, var(--photo-mid) 40%, #3a0f07 75%, var(--flyer-bg) 100%);
  }
  .terms {
    position: absolute; left: 63px; top: 872px; width: 445px;
    font-family: "Arimo", sans-serif; color: var(--ink-soft);
  }
  .terms__title {
    display: inline-block; font-size: 13px;
    padding-bottom: 2px; border-bottom: 1px solid var(--ink-soft);
    margin-bottom: 12px;
  }
  .terms__list { list-style: none; font-size: 12.4px; line-height: 16px; }
  .terms__list li { position: relative; padding-left: 18px; }
  .terms__list li::before {
    content: ""; position: absolute; left: 3px; top: 5px;
    width: 5px; height: 5px; background: var(--ink-soft);
  }
  .terms__notice {
    margin-top: 10px; font-size: 12.4px; line-height: 16px;
    font-weight: 700; color: var(--ink);
  }
  .valid-until {
    position: absolute; left: 63px; top: 1153px;
    width: 436px; height: 44px;
    background: var(--valid-bar);
    font-family: "Arimo", sans-serif; font-size: 13px;
    color: var(--ink-soft); padding: 15px 18px;
  }
</style>
</head>
<body>
  <main class="flyer">
    <div class="brand-band"></div>
    <div class="brand-name brand-name--top">Ember</div>
    <div class="brand-tag">RESTAURANT</div>
    <div class="brand-name brand-name--bottom">Nook</div>

    <h1 class="headline">
      <div class="headline__free">FREE !</div>
      <div class="headline__main">welcome cocktail</div>
      <div class="headline__sub">on your next visit *</div>
    </h1>

    <div class="photo" role="img" aria-label="Photo of three red cocktails with orange peel and mint garnish on a dark wooden bar"></div>

    <section class="terms">
      <div class="terms__title">* Terms &amp; Conditions</div>
      <ul class="terms__list">
        <li>1 free cocktail for every main course ordered from our evening menu over the value of 9.95 €&nbsp; (not including taxes).</li>
        <li>The number of free cocktails cannot exceed the number of main courses ordered from your previous visit.</li>
        <li>This offer is only valid when you present both this flyer and your receipt from your previous visit.</li>
        <li>This offer does not include ice cream cocktails. This offer cannot be used in conjunction with any other offer or promotion.</li>
        <li>Limit 1 free cocktail per person.</li>
        <li>We reserve the right to final interpretation of this offer and can cancel the offer at any time.</li>
      </ul>
      <p class="terms__notice">Please present this flyer along with your bill from your previous visit upon arrival.</p>
    </section>

    <div class="valid-until">VALID UNTIL :</div>
  </main>
</body>
</html>
```